Real Estate Investing company needs a business card design

We need a business card design for new Real Estate Investment Company called "Maple Ridge Ventures, LLC." We buy homes for cash and close quickly in any situation. Our company provides an easy and fast option for home owners who are in tough situations who need to sell their home fast and don't want realtor fees or other listing hassles. We also renovate and resell our homes which helps provide housing for the community. We would like to see designs that use the colors blue and white to match our company logo or other colors that may match our company logo. The final design should communicate trust and easy process.
Industry/Entity Type
Business
Contact Information for Business Card
Front should have company name and company logo. back of card should have company logo and area to list services.
Look and feel

```html
<!DOCTYPE html>
<html lang="en">
<head>
<meta charset="utf-8">
<title>Maple Ridge Ventures – Business Card</title>
<link rel="stylesheet" href="https://fonts.googleapis.com/css2?family=Open+Sans:wght@400;600;800&display=swap">
<style>
  :root {
    --blue: #1f8fcd;
    --blue-deep: #0f6fae;
    --blue-light: #2ea6e0;
    --white: #ffffff;
    --card-white: #f4f5f6;
    --grey-swoosh: #e3e5e7;
    --backdrop: #e9ecef;
  }
  * { box-sizing: border-box; margin: 0; padding: 0; }
  html, body { width: 1200px; height: 780px; overflow: hidden; }
  body {
    background: var(--backdrop);
    font-family: "Open Sans", Arial, sans-serif;
    position: relative;
  }
  .card {
    position: absolute;
    width: 520px;
    height: 300px;
    border-radius: 16px;
    overflow: hidden;
    box-shadow: 0 6px 18px rgba(0,0,0,0.18);
  }
  .card-front { left: 45px; top: 240px; background: var(--card-white); }
  .card-back {
    left: 635px; top: 240px;
    background: radial-gradient(ellipse at 60% 40%, var(--blue-light) 0%, var(--blue) 55%, var(--blue-deep) 100%);
    color: var(--white);
  }
  .front-wave { position: absolute; inset: 0; width: 100%; height: 100%; }

  .brand {
    display: flex;
    align-items: center;
    gap: 10px;
    font-weight: 800;
    text-transform: uppercase;
    letter-spacing: 0.5px;
    line-height: 1.1;
  }
  .brand-mark { width: 14px; height: 14px; flex: none; }

  .front-brand {
    position: absolute; left: 34px; top: 82px;
    width: 240px;
    align-items: flex-start;
    color: var(--blue); font-size: 28px;
  }
  .front-brand .brand-mark { background: var(--blue); margin-top: 9px; }

  .person { position: absolute; left: 34px; top: 182px; color: var(--blue); }
  .person-name { font-size: 19px; font-weight: 400; }
  .person-title { font-size: 13px; font-weight: 400; margin-top: 2px; }

  .contact {
    position: absolute; right: 26px; top: 30px;
    color: var(--white); font-size: 12.5px; line-height: 1.7;
    text-align: right;
  }
  .contact-icons { display: flex; gap: 5px; justify-content: flex-end; margin-bottom: 4px; }
  .contact-icon {
    width: 16px; height: 16px; border-radius: 4px;
    background: var(--white);
    display: flex; align-items: center; justify-content: center;
  }

  .back-brand {
    position: absolute; left: 0; right: 0; top: 58px;
    justify-content: center;
    color: var(--white); font-size: 30px;
  }
  .back-brand .brand-mark { background: var(--white); }

  .services { position: absolute; left: 44px; top: 138px; }
  .services-title {
    font-size: 14px; font-weight: 400; text-transform: uppercase;
    letter-spacing: 0.5px; margin-bottom: 10px;
  }
  .services-list { list-style: none; font-size: 12.5px; line-height: 1.75; }
</style>
</head>
<body>

  <section class="card card-front" aria-label="Business card front">
    <svg class="front-wave" viewBox="0 0 520 300" aria-hidden="true">
      <path d="M90,300 C170,290 220,240 240,160 C236,240 200,290 150,300 Z" fill="var(--grey-swoosh)"/>
      <path d="M160,300 C240,275 265,205 275,140 C283,85 292,40 312,10 C302,45 296,90 289,145 C279,215 250,280 192,300 Z" fill="var(--blue)"/>
      <path d="M318,0 L520,0 L520,300 L205,300 C275,270 295,205 305,140 C313,85 315,35 318,0 Z" fill="var(--blue)"/>
    </svg>

    <div class="brand front-brand">
      <span class="brand-mark"></span>
      <span class="brand-name">Maple Ridge Ventures</span>
    </div>

    <div class="person">
      <p class="person-name">Employee Name</p>
      <p class="person-title">Director</p>
    </div>

    <div class="contact">
      <div class="contact-icons">
        <span class="contact-icon">
          <svg width="10" height="10" viewBox="0 0 10 10" aria-label="Phone" role="img"><path d="M2,1 L4,1 L4.5,3 L3.5,4 C4,5.2 4.8,6 6,6.5 L7,5.5 L9,6 L9,8 C5,8.5 1.5,5 2,1 Z" fill="var(--blue)"/></svg>
        </span>
        <span class="contact-icon">
          <svg width="10" height="10" viewBox="0 0 10 10" aria-label="Email" role="img"><rect x="1" y="2.5" width="8" height="5" fill="none" stroke="var(--blue)" stroke-width="1"/><path d="M1,2.5 L5,5.5 L9,2.5" fill="none" stroke="var(--blue)" stroke-width="1"/></svg>
        </span>
        <span class="contact-icon">
          <svg width="10" height="10" viewBox="0 0 10 10" aria-label="Website" role="img"><circle cx="5" cy="5" r="3.8" fill="none" stroke="var(--blue)" stroke-width="1"/><path d="M1.2,5 H8.8 M5,1.2 V8.8" stroke="var(--blue)" stroke-width="0.9"/></svg>
        </span>
      </div>
      <p>000-000-0000</p>
      <p>hello@mapleridge.co.nz</p>
      <p>www.mapleridge.co.nz</p>
    </div>
  </section>

  <section class="card card-back" aria-label="Business card back">
    <div class="brand back-brand">
      <span class="brand-mark"></span>
      <span class="brand-name">Maple Ridge Ventures</span>
    </div>

    <div class="services">
      <h2 class="services-title">Services</h2>
      <ul class="services-list">
        <li>Cash home buying / Fast closings and flexible terms</li>
        <li>Renovation and resale / Foreclosure help and relocation</li>
        <li>Inherited homes / As-is purchases and fair offers</li>
      </ul>
    </div>
  </section>

</body>
</html>
```